Lumo Ket

Need business cards designed. Project is an Arts Center in Hollywood. It'll include 3 live theatre, a restaurant and event space.

Target Market(s)

Across the board, young and old.

Industry/Entity Type

Entertainment

Contact Information for Business Card

Be creative. This is a creative venture that I'm building.

```html
<!DOCTYPE html>
<html lang="en">
<head>
<meta charset="utf-8">
<title>Lumo Ket – Business Cards</title>
<link rel="stylesheet" href="https://fonts.googleapis.com/css2?family=Cinzel:wght@400&family=Montserrat:wght@400&display=swap">
<style>
  :root{
    --backdrop:#4d4d47;
    --card-edge:#141414;
    --card-ink:#000000;
    --gold:#f0c850;
    --white:#ffffff;
    --soft-white:#e6e6e6;
  }
  *{box-sizing:border-box;margin:0;padding:0}
  html,body{width:1200px;height:900px;overflow:hidden;background:var(--backdrop)}
  .canvas{position:relative;width:1200px;height:900px}

  .card{position:absolute;background:var(--card-edge);padding:9px}
  .card__face{position:relative;width:100%;height:100%;background:var(--card-ink);overflow:hidden}

  .card--front{left:174px;top:178px;width:457px;height:281px}
  .card--back{left:314px;top:490px;width:456px;height:280px}

  .hero-photo{position:absolute;left:0;top:0;width:100%;height:208px;
    background:
      radial-gradient(ellipse at 52% 55%, #8a8a8a 0%, #4a4a4a 28%, #1c1c1c 60%, #050505 100%);}

  .wordmark{font-family:'Cinzel',serif;font-weight:400;color:var(--gold);white-space:nowrap;line-height:1}
  .wordmark--front{position:absolute;right:30px;top:32px;font-size:40px;text-align:right;line-height:0.95}
  .wordmark--back{position:absolute;left:0;right:0;top:100px;font-size:42px;text-align:center}

  .holder-name{position:absolute;left:32px;top:189px;font-family:'Cinzel',serif;font-size:16px;
    color:var(--white);letter-spacing:0.5px}
  .contact{position:absolute;top:234px;font-family:'Montserrat',sans-serif;font-size:11px;
    color:var(--soft-white);line-height:15px}
  .contact--direct{left:27px}
  .contact--place{left:197px}
  .contact__row{display:flex;align-items:center;gap:6px}
  .contact__row svg{flex:none}
  .contact__indent{padding-left:16px}

  .back-glow{position:absolute;inset:0;
    background:radial-gradient(ellipse at 50% 45%, #2a2418 0%, #0d0b08 40%, #000 75%)}
  .web-address{position:absolute;left:0;right:0;top:186px;text-align:center;
    font-family:'Montserrat',sans-serif;font-size:11px;letter-spacing:4px;color:var(--soft-white)}

  .display-mark{position:absolute;left:690px;top:90px;width:440px;text-align:center;
    font-size:140px;line-height:1.05}
</style>
</head>
<body>
<main class="canvas">

  <section class="card card--front" aria-label="Card front">
    <div class="card__face">
      <div class="hero-photo" role="img" aria-label="Night render of the arts center building with film stills projected on its facade"></div>
      <div class="wordmark wordmark--front">Lumo<br>Ket</div>
      <p class="holder-name">Daniel Arvo | Lumo Ket</p>
      <div class="contact contact--direct">
        <div class="contact__row">
          <svg width="11" height="9" viewBox="0 0 11 9" aria-hidden="true"><path d="M1 3 Q5.5 0 10 3 L9 4.5 L7.5 3.5 L3.5 3.5 L2 4.5 Z M2.5 5 L8.5 5 L9.5 8.5 L1.5 8.5 Z" fill="var(--soft-white)"/></svg>
          <span>555.240.0148</span>
        </div>
        <div class="contact__row">
          <svg width="11" height="9" viewBox="0 0 11 9" aria-hidden="true"><rect x="0.5" y="0.5" width="10" height="8" fill="none" stroke="var(--soft-white)"/><path d="M0.5 0.5 L5.5 5 L10.5 0.5" fill="none" stroke="var(--soft-white)"/></svg>
          <span>darvo@lumoket.com</span>
        </div>
      </div>
      <div class="contact contact--place">
        <div class="contact__row">
          <svg width="10" height="14" viewBox="0 0 10 14" aria-hidden="true"><path d="M5 13 C2 9 1 7 1 5 A4 4 0 0 1 9 5 C9 7 8 9 5 13 Z" fill="none" stroke="var(--soft-white)" stroke-width="1.4"/><circle cx="5" cy="5" r="1.5" fill="var(--soft-white)"/></svg>
          <span>415 Linden Row</span>
        </div>
        <div class="contact__indent">Castell Park, ST 00417</div>
      </div>
    </div>
  </section>

  <section class="card card--back" aria-label="Card back">
    <div class="card__face">
      <div class="back-glow"></div>
      <div class="wordmark wordmark--back">Lumo Ket</div>
      <p class="web-address">www.lumoket.com</p>
    </div>
  </section>

  <div class="wordmark display-mark">Lumo<br>Ket</div>

</main>
</body>
</html>
```